Calder Pizza - Takeout Menu Design

We are looking for a takeout menu design.
We are looking for a( 5" x 8.5" DOUBLE SIDED) flyer with our available pizza flavors
Must be easy to ready and not "busy"

Must include our logo (attached)
website: www.calderpizza.ca
address:
Fenwick Ridge Plaza
417, 318 9 Avenue SW
and the following details:
Visit our website for our complete appetizer, pasta, salad and catering menu.

Winner of this contest will also be offered to create a few print designs via printhive.

Please do not hesitate to ask any questions.

Target Market(s)

Business / Office clientele

Industry/Entity Type

Pizza place / specializing in corporate orders

Requirements
Must have
• Easy to read
Should not have
• Can not be busy or cluttered

```html
<!DOCTYPE html>
<html lang="en">
<head>
<meta charset="utf-8">
<title>Calder Pizza – Take-Out Menu</title>
<link rel="stylesheet" href="https://fonts.googleapis.com/css2?family=Poppins:wght@300;400;500&family=Bungee&display=swap">
<style>
  :root {
    --board: #262626;
    --board-light: #323232;
    --ink: #f2f2f2;
    --ink-soft: #d9d9d9;
    --accent: #c0301f;
    --rule: #9a9a9a;
  }
  * { margin: 0; padding: 0; box-sizing: border-box; }
  html, body { width: 720px; height: 1200px; overflow: hidden; }
  body {
    position: relative;
    background: radial-gradient(ellipse at 40% 40%, var(--board-light), var(--board) 70%);
    color: var(--ink);
    font-family: "Poppins", sans-serif;
  }
  .hero-photo { position: absolute; top: 0; right: 0; width: 350px; height: 240px; }
  .brand {
    position: absolute;
    left: 34px; top: 46px;
    font-weight: 300;
    font-size: 46px;
    letter-spacing: 1px;
    line-height: 1;
    text-transform: uppercase;
    color: var(--ink);
  }
  .section-title {
    position: absolute;
    font-family: "Bungee", sans-serif;
    font-weight: 400;
    color: var(--accent);
    white-space: nowrap;
    transform: translateX(-50%);
  }
  .menu-title { left: 188px; top: 134px; font-size: 20px; }
  .tagline {
    position: absolute;
    left: 188px; top: 174px;
    transform: translateX(-50%);
    text-align: center;
    font-size: 15.5px;
    line-height: 18.5px;
    white-space: nowrap;
  }
  .heading-classic { left: 188px; top: 257px; font-size: 16.5px; }
  .heading-specialty-left { left: 188px; top: 647px; font-size: 16.5px; }
  .heading-specialty-right { left: 531px; top: 257px; font-size: 16.5px; }
  .size-label { position: absolute; font-size: 16px; font-weight: 500; transform: translateX(-50%); }
  .item { position: absolute; width: 320px; }
  .col-left .item { left: 34px; }
  .col-right .item { left: 377px; }
  .item-name { font-size: 15px; font-weight: 400; line-height: 20px; white-space: nowrap; }
  .item-desc {
    font-size: 9px;
    line-height: 9.5px;
    letter-spacing: -0.25px;
    color: var(--ink-soft);
    white-space: nowrap;
  }
  .price { position: absolute; top: 0; font-size: 15px; line-height: 20px; font-weight: 500; }
  .price-small { left: 200px; }
  .price-large { left: 257px; }
  .item-note .item-desc { padding-top: 5px; }
  .footer {
    position: absolute;
    left: 377px; top: 1126px;
    width: 308px;
    border-top: 1.5px solid var(--rule);
    text-align: center;
    font-size: 10px;
    line-height: 12px;
    padding-top: 4px;
  }
  .footer .web { margin-top: 4px; }
</style>
</head>
<body>
  <svg class="hero-photo" viewBox="0 0 350 240" role="img" aria-label="Photo of a pizza with peppers, olives, ham and mushrooms">
    <defs>
      <radialGradient id="pizzaTone" cx="0.45" cy="0.4" r="0.6">
        <stop offset="0" stop-color="#d9a05a"/>
        <stop offset="0.6" stop-color="#c77a3a"/>
        <stop offset="1" stop-color="#b8723c"/>
      </radialGradient>
    </defs>
    <circle cx="192" cy="40" r="192" fill="var(--accent)"/>
    <circle cx="210" cy="30" r="186" fill="url(#pizzaTone)"/>
  </svg>

  <div class="brand">Calder Pizza</div>

  <h2 class="section-title menu-title">Menu</h2>
  <p class="tagline">All of our pizzas are prepared fresh<br>everyday using only the finest<br>mozzarella blend and ingredients</p>

  <h2 class="section-title heading-classic">Classic Take-Out Pizza</h2>
  <span class="size-label" style="left:257px;top:289px">8"</span>
  <span class="size-label" style="left:319px;top:289px">13"</span>

  <div class="col-left">
    <div class="item" style="top:326px"><h3 class="item-name">Pepperoni &amp; Mushroom</h3><span class="price price-small">$12.99</span><span class="price price-large">$30.95</span></div>
    <div class="item" style="top:364px"><h3 class="item-name">Pepperoni</h3><span class="price price-small">$11.99</span><span class="price price-large">$29.95</span></div>
    <div class="item" style="top:402px"><h3 class="item-name">Hawaiian</h3><span class="price price-small">$12.99</span><span class="price price-large">$30.95</span></div>
    <div class="item" style="top:440px"><h3 class="item-name">Beef &amp; Mushroom</h3><span class="price price-small">$13.49</span><span class="price price-large">$32.95</span></div>
    <div class="item" style="top:478px"><h3 class="item-name">Pepperoni &amp; Ham</h3><span class="price price-small">$12.99</span><span class="price price-large">$30.95</span></div>
    <div class="item" style="top:516px"><h3 class="item-name">Ham &amp; Mushroom</h3><span class="price price-small">$12.99</span><span class="price price-large">$30.95</span></div>
    <div class="item" style="top:555px"><h3 class="item-name">Beef &amp; Onion</h3><span class="price price-small">$13.49</span><span class="price price-large">$32.95</span></div>
    <div class="item" style="top:592px"><h3 class="item-name">Cheese</h3><span class="price price-small">$11.99</span><span class="price price-large">$29.95</span></div>
  </div>

  <h2 class="section-title heading-specialty-left">Specialty Take-Out Pizza</h2>
  <span class="size-label" style="left:257px;top:678px">8"</span>
  <span class="size-label" style="left:319px;top:678px">13"</span>

  <div class="col-left">
    <div class="item" style="top:705px"><h3 class="item-name">All Meat</h3><p class="item-desc">Pepperoni, Beef &amp; Smoked Ham &amp; Becon</p><span class="price price-small">$14.99</span><span class="price price-large">$35.95</span></div>
    <div class="item" style="top:747px"><h3 class="item-name">Double Pepperoni</h3><p class="item-desc">Loads of Pepperoni</p><span class="price price-small">$13.49</span><span class="price price-large">$32.95</span></div>
    <div class="item" style="top:787px"><h3 class="item-name">Hot Honey Pepperoni</h3><p class="item-desc">Double Pepperoni &amp; drizzled with Hot<br>Honey</p><span class="price price-small">$14.49</span><span class="price price-large">$34.95</span></div>
    <div class="item" style="top:836px"><h3 class="item-name">Hawaiian Heat</h3><p class="item-desc">Smoked Ham, Pineapple &amp; Banana<br>Peppers</p><span class="price price-small">$13.49</span><span class="price price-large">$32.95</span></div>
    <div class="item" style="top:886px"><h3 class="item-name">Four Cheese</h3><p class="item-desc">Mozzarella, Feta, Romano &amp; Cheddar<br>Cheese</p><span class="price price-small">$13.49</span><span class="price price-large">$32.95</span></div>
    <div class="item" style="top:935px"><h3 class="item-name">Montreal</h3><p class="item-desc">Pepperoni &amp; Double Smoked Bacon</p><span class="price price-small">$13.49</span><span class="price price-large">$32.95</span></div>
    <div class="item" style="top:976px"><h3 class="item-name">Montreal Heat</h3><p class="item-desc">Pepperoni &amp; Double Smoked Bacon &amp;<br>Banana Peppers</p><span class="price price-small">$13.99</span><span class="price price-large">$33.95</span></div>
    <div class="item" style="top:1025px"><h3 class="item-name">Supreme</h3><p class="item-desc">Pepperoni, Mushrooms &amp; Green Peppers</p><span class="price price-small">$13.49</span><span class="price price-large">$32.95</span></div>
    <div class="item" style="top:1065px"><h3 class="item-name">Canadian</h3><p class="item-desc">Pepperoni, Mushrooms &amp; Ham</p><span class="price price-small">$13.49</span><span class="price price-large">$32.95</span></div>
    <div class="item" style="top:1108px"><h3 class="item-name">BBQ Chicken</h3><p class="item-desc">Chicken Breast, Hickory BBQ Sauce &amp;<br>Red Onions</p><span class="price price-small">$13.99</span><span class="price price-large">$33.95</span></div>
  </div>

  <h2 class="section-title heading-specialty-right">Specialty Take-Out Pizza</h2>
  <span class="size-label" style="left:598px;top:287px">8"</span>
  <span class="size-label" style="left:660px;top:287px">13"</span>

  <div class="col-right">
    <div class="item" style="top:326px"><h3 class="item-name">BBQ Chicken Plus</h3><p class="item-desc">Chicken Breast, Hickory BBQ Sauce<br>Red Onions &amp; Cilantro</p><span class="price price-small">$14.79</span><span class="price price-large">$34.95</span></div>
    <div class="item" style="top:376px"><h3 class="item-name">Spicy BBQ Chicken</h3><p class="item-desc">Chicken Breast, Hickory BBQ Sauce<br>Red Onions &amp; Banana Peppers</p><span class="price price-small">$14.49</span><span class="price price-large">$35.95</span></div>
    <div class="item" style="top:425px"><h3 class="item-name">Sweet Chili Chicken</h3><p class="item-desc">Chicken Breast, Pineapple, Red Onions<br>&amp; Sweet Chili Sauce</p><span class="price price-small">$14.49</span><span class="price price-large">$35.95</span></div>
    <div class="item" style="top:475px"><h3 class="item-name">Chicken Club</h3><p class="item-desc">Chicken Breast, Double Smoked Bacon<br>Red Onions &amp; Tomatoes</p><span class="price price-small">$14.79</span><span class="price price-large">$35.95</span></div>
    <div class="item" style="top:524px"><h3 class="item-name">Athenean</h3><p class="item-desc">Chicken Breast, Spinach, Feta Cheese<br>&amp; Tomato</p><span class="price price-small">$14.49</span><span class="price price-large">$34.95</span></div>
    <div class="item" style="top:573px"><h3 class="item-name">Greek Supreme</h3><p class="item-desc">Chicken Breast, Feta Cheese, Tomato<br>Green Pepper, Red Onions &amp; Black Olives</p><span class="price price-small">$14.99</span><span class="price price-large">$35.95</span></div>
    <div class="item" style="top:623px"><h3 class="item-name">Mediterranean Chicken</h3><p class="item-desc">Seasoned Chicken Breast, Tomatoes<br>Red Onions &amp; Feta Cheese</p><span class="price price-small">$14.99</span><span class="price price-large">$35.95</span></div>
    <div class="item" style="top:672px"><h3 class="item-name">Original Spinach</h3><p class="item-desc">Spinach &amp; Feta Cheese</p><span class="price price-small">$13.49</span><span class="price price-large">$32.95</span></div>
    <div class="item" style="top:713px"><h3 class="item-name">Zeus</h3><p class="item-desc">Spinach, Feta Cheese &amp;Tomatoes</p><span class="price price-small">$13.95</span><span class="price price-large">$33.95</span></div>
    <div class="item" style="top:752px"><h3 class="item-name">Greek</h3><p class="item-desc">Feta Cheese, Tomato, Green Peppers<br>Red Onions &amp; Black Olives</p><span class="price price-small">$13.99</span><span class="price price-large">$33.95</span></div>
    <div class="item" style="top:802px"><h3 class="item-name">Vegetarian</h3><p class="item-desc">Mushrooms, Tomatoes, Green Peppers<br>&amp; Black Olives</p><span class="price price-small">$13.49</span><span class="price price-large">$32.95</span></div>
    <div class="item" style="top:852px"><h3 class="item-name">Veggie Delight</h3><p class="item-desc">Mushrooms, Tomatoes, Green Peppers<br>Black Olives &amp; Onions</p><span class="price price-small">$13.95</span><span class="price price-large">$33.95</span></div>
    <div class="item" style="top:901px"><h3 class="item-name">Deluxe</h3><p class="item-desc">Pepperoni, Mushrooms, Ham, Tomatoes<br>Green Peppers &amp; Red Onions</p><span class="price price-small">$14.49</span><span class="price price-large">$34.95</span></div>
    <div class="item" style="top:951px"><h3 class="item-name">Calder Special</h3><p class="item-desc">Pepperoni, Mushrooms, Ham, Green<br>Peppers &amp; Black Olives</p><span class="price price-small">$14.49</span><span class="price price-large">$34.95</span></div>
    <div class="item" style="top:1000px"><h3 class="item-name">Dill Pickle</h3><p class="item-desc">Crispy Dill Pickles, Fresh Dill with our<br>cream based garlic sauce</p><span class="price price-small">$13.49</span><span class="price price-large">$32.95</span></div>
    <div class="item item-note" style="top:1041px"><p class="item-desc">Served with our without bacon</p><span class="price price-small">$14.49</span><span class="price price-large">$35.95</span></div>
    <div class="item" style="top:1069px"><h3 class="item-name">BBQ Pulled Pork</h3><p class="item-desc">Pulled Pork, Red Onions, Red Peppers<br>&amp; Cilantro</p><span class="price price-small">$14.49</span><span class="price price-large">$35.95</span></div>
  </div>

  <footer class="footer">
    <p>Fenwick Ridge Plaza</p>
    <p>417, 318 9 Avenue SW</p>
    <p class="web">www.calderpizza.ca</p>
  </footer>
</body>
</html>
```